Property management company looking for modern card design

We at Blue Maple Holdings provides property management services for its residential and commercial properties, with expertise in all categories of multifamily, industrial and office projects throughout California.

We need a business card design that is professional and modern designed business card. In our field, clients get hundreds of business cards, we would like our card to stand out.

Please avoid small print.

Target Market(s)

Professionals and high end clients

Industry/Entity Type

Financial Planning

Contact Information for Business Card

Company Name: Blue Maple Holdings, Name, email, license #, phone number, website bluemapleholdings.example

Font styles to use
Sans Serif

Requirements
Must have
• The card design needs to be adaptable because there is a possibly we will be expanding into different sectors other than real estate. The card design should be focused on financial planning and asset management.
Nice to have
• Modern and simple business card. Eye catching. Non-standard size/shaped cards would be great.
• bluemapleholdings.example
Should not have
• Too many bright color or any pictures or shapes of real estate stuff.

```html
<!DOCTYPE html>
<html lang="en">
<head>
<meta charset="utf-8">
<title>Blue Maple Holdings – Business Card</title>
<link rel="stylesheet" href="https://fonts.googleapis.com/css2?family=Roboto:wght@400;500;700&display=swap">
<style>
  :root {
    --stage: #2b2b2b;
    --card: #ffffff;
    --accent: #e8262b;
    --accent-soft: #fde4dc;
    --ink: #222222;
    --ink-mid: #333333;
    --brand-grey: #4a4a4d;
    --rule: #555555;
  }
  * { margin: 0; padding: 0; box-sizing: border-box; }
  html, body { width: 1200px; height: 900px; overflow: hidden; }
  body {
    background: var(--stage);
    font-family: "Roboto", Arial, sans-serif;
    position: relative;
  }
  .card {
    position: absolute;
    left: 316px;
    width: 592px;
    height: 346px;
    background: var(--card);
    border-radius: 18px;
    overflow: hidden;
  }
  .card--front { top: 87px; }
  .card--back { top: 481px; }

  /* Front */
  .brand-block {
    position: absolute;
    left: 74px; top: 98px;
    width: 190px;
    display: flex; flex-direction: column; align-items: center;
    gap: 14px;
  }
  .brand-dot {
    width: 64px; height: 64px; border-radius: 50%;
    background: var(--accent);
  }
  .brand-name {
    font-weight: 700; font-size: 20px; line-height: 1.2;
    color: var(--accent); text-align: center;
  }
  .divider {
    position: absolute; left: 295px; top: 103px;
    width: 2px; height: 136px; background: var(--rule);
  }
  .person {
    position: absolute; left: 339px; top: 106px;
  }
  .person__name { font-size: 22px; font-weight: 500; color: var(--ink); line-height: 1.1; }
  .person__title { font-size: 13px; color: var(--accent); margin-top: 2px; }
  .contact { list-style: none; margin-top: 17px; }
  .contact li {
    display: flex; align-items: center; gap: 8px;
    font-size: 14px; color: var(--ink-mid);
    height: 18.5px;
  }
  .contact svg { width: 12px; height: 12px; fill: var(--accent); flex: none; }
  .address {
    position: absolute; left: 0; right: 0; top: 300px;
    text-align: center; font-size: 14px; color: var(--ink-mid);
  }

  /* Back */
  .backdrop-circle {
    position: absolute; left: -230px; top: -40px;
    width: 500px; height: 420px; border-radius: 50%;
    background: var(--accent-soft);
  }
  .wordmark {
    position: absolute; left: 0; right: 0; top: 140px;
    text-align: center;
  }
  .wordmark__name {
    font-weight: 700; font-size: 33px; letter-spacing: 0.5px;
    color: var(--brand-grey); text-transform: uppercase;
  }
  .wordmark__rule {
    width: 294px; height: 1px; background: var(--brand-grey);
    margin: 10px auto 0;
  }
</style>
</head>
<body>

<section class="card card--front">
  <div class="brand-block">
    <span class="brand-dot"></span>
    <span class="brand-name">Blue Maple Holdings</span>
  </div>
  <span class="divider"></span>
  <div class="person">
    <p class="person__name">Daniel Reyes</p>
    <p class="person__title">Managing director</p>
    <ul class="contact">
      <li><svg viewBox="0 0 24 24"><path d="M6.6 10.8a15.1 15.1 0 0 0 6.6 6.6l2.2-2.2c.3-.3.7-.4 1-.2 1.1.4 2.3.6 3.6.6.6 0 1 .4 1 1V20c0 .6-.4 1-1 1A17 17 0 0 1 3 4c0-.6.4-1 1-1h3.5c.6 0 1 .4 1 1 0 1.3.2 2.5.6 3.6.1.3 0 .7-.2 1z"/></svg>0555-0148-2291</li>
      <li><svg viewBox="0 0 24 24"><path d="M6 2h12v5H6zM3 8h18a1 1 0 0 1 1 1v8h-4v5H6v-5H2V9a1 1 0 0 1 1-1zm5 7v5h8v-5z"/></svg>0555-0193-6402</li>
      <li><svg viewBox="0 0 24 24"><path d="M2 5h20v14H2zm2 2v.5l8 5 8-5V7l-8 5z"/></svg>dreyes@bluemapleholdings.example</li>
      <li><svg viewBox="0 0 24 24"><path d="M2 4h20v13H2zm2 2v9h16V6zM8 19h8v2H8z"/></svg>bluemapleholdings.example</li>
    </ul>
  </div>
  <p class="address">2480 Harbor Avenue, Suite 210, City, State, Zip Code</p>
</section>

<section class="card card--back">
  <span class="backdrop-circle"></span>
  <div class="wordmark">
    <p class="wordmark__name">Blue Maple Holdings</p>
    <div class="wordmark__rule"></div>
  </div>
</section>

</body>
</html>
```